Looking for a modern, Professional business card design

We have a simple business card, but are looking for a more modern, professional look. A sample of the basic card is attached as well as the logo. We would also like to add that we offer:
Struggling with your finances?
- Learn to become debt free
- Discover the power of cash
- Control your money instead of it controlling you
Let us help you achieve a new level of financial freedom!
Also, we would like to have a "SPECIAL OFFER!: FREE 30 minute consultation"
Financial Planning

```html
<!DOCTYPE html>
<html lang="en">
<head>
<meta charset="UTF-8">
<title>Liberty Path Coaching – Business Card</title>
<link rel="stylesheet" href="https://fonts.googleapis.com/css2?family=Open+Sans:wght@400;600;700&display=swap">
<style>
  :root {
    --stage: #2a2829;
    --green-light: #8cc04a;
    --green-mid: #5fa63c;
    --green-deep: #2f7a30;
    --paper: #f2f2f2;
    --ink-light: #ffffff;
  }
  * { margin: 0; padding: 0; box-sizing: border-box; }
  html, body {
    width: 1200px;
    height: 759px;
    overflow: hidden;
    background: var(--stage);
    font-family: "Open Sans", Arial, sans-serif;
  }
  .stage {
    width: 1200px;
    height: 759px;
    display: flex;
    align-items: center;
    justify-content: center;
  }
  .card {
    position: relative;
    width: 980px;
    height: 560px;
    border-radius: 40px;
    overflow: hidden;
    background:
      radial-gradient(ellipse at 25% 30%, rgba(160, 210, 90, 0.55) 0%, rgba(160, 210, 90, 0) 55%),
      linear-gradient(135deg, var(--green-light) 0%, var(--green-mid) 50%, var(--green-deep) 100%);
    color: var(--ink-light);
  }
  .corner-tab {
    position: absolute;
    width: 250px;
    height: 26px;
    background: var(--paper);
  }
  .corner-tab--top { top: 0; right: 0; border-bottom-left-radius: 26px; }
  .corner-tab--bottom { bottom: 0; left: 0; border-top-right-radius: 26px; }

  .card__content {
    position: absolute;
    left: 70px;
    right: 70px;
    top: 62px;
    display: flex;
    flex-direction: column;
  }

  .brand {
    display: flex;
    align-items: center;
    gap: 18px;
  }
  .brand__dot {
    width: 44px;
    height: 44px;
    border-radius: 50%;
    background: var(--ink-light);
    flex-shrink: 0;
  }
  .brand__name {
    font-weight: 700;
    font-size: 40px;
    line-height: 1.05;
    letter-spacing: 1px;
    text-transform: uppercase;
  }
  .brand__tagline {
    margin: 8px 0 0 62px;
    font-size: 14px;
    font-weight: 400;
    opacity: 0.9;
  }

  .pitch { margin-top: 26px; }
  .pitch__headline {
    font-weight: 700;
    font-size: 34px;
    line-height: 1.2;
    margin-bottom: 8px;
  }
  .pitch__list {
    list-style: none;
    font-weight: 600;
    font-size: 20px;
    line-height: 1.4;
    margin-left: 40px;
  }
  .pitch__list li::before { content: "- "; }
  .pitch__closing {
    margin-left: 40px;
    font-size: 20px;
    line-height: 1.4;
    font-weight: 400;
  }

  .offer {
    margin: 18px 0 0 80px;
    font-size: 20px;
    line-height: 1.4;
  }
  .offer__highlight { font-weight: 700; font-size: 23px; }
</style>
</head>
<body>
  <main class="stage">
    <section class="card" aria-label="Business card front">
      <div class="corner-tab corner-tab--top"></div>
      <div class="corner-tab corner-tab--bottom"></div>

      <div class="card__content">
        <div class="brand">
          <span class="brand__dot"></span>
          <span class="brand__name">Liberty Path<br>Coaching</span>
        </div>
        <p class="brand__tagline">Achieve a new level of personal freedom</p>

        <div class="pitch">
          <h1 class="pitch__headline">Struggling with your finances?</h1>
          <ul class="pitch__list">
            <li>Learn to become debt free</li>
            <li>Discover the power of cash</li>
            <li>Control your money instead of it controlling you</li>
          </ul>
          <p class="pitch__closing">Let us help you achieve a new level of financial freedom!</p>
        </div>

        <p class="offer">
          Also, we would like to have a <span class="offer__highlight">"SPECIAL OFFER!</span><br>
          <span class="offer__highlight">FREE 30</span> minute consultation.
        </p>
      </div>
    </section>
  </main>
</body>
</html>
```